QVT Web Design Project

I would like a simple and elegant design for my international business consulting practice web site. I already have new QVT Logo and will have brochure-colors are blue, green and black

Practice areas:
I offer consulting services specializing in developing Internet-based anti-counterfeiting and anti-fraud programs, test purchases and investigations.

I offer Cyber Security, Data Protection and Compliance services

I also offer International Due Diligence Investigations and Country and Travel Risk Assessments

General Background Investigations

Physical Security Services

About me section listing my Bio

I have a set of key associates that I work with around the world and will want to list their CVs or Bios under "QVT

Associates"Banner with nice photo but not too cluttered

Ability to Upload documents and articles

Contact us section
Updates

I have uploaded my new logo-please advise if you didn't get it or it is not in the correct file format.

Thank you

Gordon

Hello Everyone,

Thank you for your submissions and ideas. I'm not sure about design only vs code. I understand that some of you do not do code-if not then please just provide design.

More about my business: see below link on Sharebox files to my brochure-this should help but don't use that phone number-see below.

https://files.sharebox.example/viewer?a=v&pid=explorer&srcid=0Q-4PX9nRfwqeMkTuZ3B8NHhsLWVmXy00ZWQ3LTkyOGQtZmQ1ZTg0YjE2OXB4&hl=en_US

 

Here are some details.

Contacts:

Gordon T. Falkirk, CPP

President

Falkirk and Associates, LLC

P.O. Box 41927

Gaithersburg, MD 20871

USA

web address:www.Falkirkandassociates.example (currently not working)

email:gord @falkirkand associates.example

Tel: 202-555-0147

I hope this is helpful. Gord

Reason: Sorry but during holiday period, have not had as much time to devote to this project. Thanks for your submissions.

Per my previous guidance, please keep designs simple and elegant and free from traditional security images with locks and chains-I prefer one or at most, two photos. Two colors- blue and green in addition to black for print. I want to present professional, corporate and international image. Thank you for your ideas nad submissions.

Gord

Target Market(s)

Law firms, large multi-national corporations, Security Industry

Industry/Entity Type

Business

Requirements
Must have
• Must have sections: (will provide text)

About QVT (will provide text)

Practice areas

Associates (will provide text)

Contact us

(it must also have ability to upload files and articles)
Should not have
• Old style fonts and symbols such as security badges, scales of justice, etc. I want a sleek and modern design.

```html
<!DOCTYPE html>
<html lang="en">
<head>
<meta charset="utf-8">
<title>Falkirk &amp; Associates, LLC</title>
<link rel="stylesheet" href="https://fonts.googleapis.com/css2?family=Open+Sans:wght@400;600;700&family=Questrial&display=swap">
<style>
:root{
  --brand-blue:#0b5aa0;
  --brand-blue-dark:#084a86;
  --link-blue:#5b9bd0;
  --text-dark:#111;
  --text-mid:#333;
  --panel-grey:#ebebeb;
  --page-grey:#e4e4e4;
  --white:#fff;
}
*{margin:0;padding:0;box-sizing:border-box}
html,body{width:1200px;height:1032px;overflow:hidden;background:var(--white)}
body{position:relative;font-family:"Open Sans",Arial,sans-serif;color:var(--text-dark)}
.abs{position:absolute}

.backdrop{position:absolute;left:0;top:0;width:1200px;height:1032px}

.brand{left:72px;top:40px}
.brand-name{font-size:23px;color:var(--brand-blue);font-weight:400;letter-spacing:.2px;white-space:nowrap}
.brand-name .mark{padding-right:10px;margin-right:8px;border-right:1px solid #9ab}
.brand-tagline{margin-top:4px;font-size:14px;letter-spacing:1.4px;color:var(--brand-blue)}

.main-nav{left:542px;top:38px;width:589px;height:53px;border:1px solid #d6d6d6;border-radius:27px;
  background:linear-gradient(#fdfdfd,#e9e9e9);display:flex;overflow:hidden}
.main-nav a{display:flex;align-items:center;justify-content:center;font-size:16px;color:#222;text-decoration:none;
  border-left:1px solid #d6d6d6}
.main-nav a:first-child{border-left:none}

.content-card{left:69px;top:131px;width:1060px;height:720px;background:var(--white);border-radius:5px;
  box-shadow:0 0 3px rgba(0,0,0,.15)}

.hero{left:87px;top:145px;width:1025px;height:295px;
  background:radial-gradient(circle at 35% 30%,#dff1fd 0,#7fc3ec 25%,#2a86c8 55%,#0d4f8c 100%);
  box-shadow:0 6px 8px rgba(0,0,0,.25)}
.hero-caption{left:625px;top:216px;width:439px;height:105px;background:rgba(255,255,255,.88);
  padding:2px 10px;font-size:20.5px;line-height:33px;color:#1b5ea8;text-align:justify;letter-spacing:.3px}

.section-band{left:63px;top:460px;width:1074px;height:59px;background:var(--brand-blue)}
.section-title{top:474px;font-family:"Questrial",Arial,sans-serif;font-size:24px;color:var(--white)}

.about-text{left:125px;top:549px;width:273px;font-size:13.3px;line-height:19.6px;text-align:justify;color:var(--text-dark)}

.associates-list{left:455px;top:557px;list-style:none;font-size:13.5px}
.associates-list li{height:33px}
.associates-list li::before{content:"> "}

.practice-list{left:781px;top:545px;width:331px;height:243px;background:var(--panel-grey);list-style:none;padding-top:6px}
.practice-list li{height:33px;line-height:32px;padding-left:15px;font-size:13.5px;color:#222;border-bottom:1px solid var(--white)}
.practice-list li:last-child{border-bottom:none}

.read-more{top:807px;font-size:14px;font-weight:700;color:var(--link-blue);text-decoration:none;display:flex;align-items:center;gap:8px}

.footer-title{top:872px;font-family:"Questrial",Arial,sans-serif;font-size:24px;color:var(--white)}
.footer-address{left:131px;top:911px;font-size:17px;line-height:24px;color:#e8f1fa}
.footer-divider{left:402px;top:908px;width:1px;height:85px;background:rgba(255,255,255,.6)}
.contact-lines{left:422px;top:911px;font-size:17px;line-height:31px;color:#e8f1fa}
.contact-lines dt{float:left;width:70px;font-weight:600;color:var(--white)}
.contact-lines dd{margin-left:70px}
.social{left:895px;font-size:17px;font-weight:700;color:var(--white);display:flex;align-items:center;gap:16px}
.social .dot{width:28px;height:28px;border-radius:50%;background:radial-gradient(circle at 40% 35%,#888,#333)}
.copyright{left:730px;top:1008px;font-size:11px;font-weight:700;color:#222}
</style>
</head>
<body>

<svg class="backdrop" viewBox="0 0 1200 1032" aria-hidden="true">
  <defs>
    <linearGradient id="greyFade" x1="0" y1="0" x2="0" y2="1">
      <stop offset="0" stop-color="#d9d9d9"/>
      <stop offset="1" stop-color="#f0f0f0"/>
    </linearGradient>
    <linearGradient id="footerFade" x1="0" y1="0" x2="0" y2="1">
      <stop offset="0" stop-color="#0b5aa0"/>
      <stop offset=".8" stop-color="#1466ad"/>
      <stop offset="1" stop-color="#6aaee0"/>
    </linearGradient>
  </defs>
  <path d="M0 268 Q600 330 1200 268 V777 H0 Z" fill="url(#greyFade)"/>
  <path d="M0 268 Q40 275 70 292" stroke="#0b5aa0" stroke-width="4" fill="none"/>
  <path d="M1130 292 Q1160 275 1200 268" stroke="#0b5aa0" stroke-width="4" fill="none"/>
  <rect x="0" y="777" width="1200" height="255" fill="url(#footerFade)"/>
</svg>

<header>
  <div class="abs brand">
    <div class="brand-name"><span class="mark">QVT</span>Falkirk &amp; Associates, LLC</div>
    <div class="brand-tagline">Intellectual Property and Cyber Security</div>
  </div>
  <nav class="abs main-nav">
    <a href="#" style="width:81px" aria-label="Home">
      <svg width="28" height="26" viewBox="0 0 28 26"><path d="M14 2 L1 13 H5 V25 H11 V17 H17 V25 H23 V13 H27 Z" fill="#1f6db3"/></svg>
    </a>
    <a href="#" style="width:118px">About QVT</a>
    <a href="#" style="width:144px">Practice areas</a>
    <a href="#" style="width:114px">Associates</a>
    <a href="#" style="width:132px">Contact us</a>
  </nav>
</header>

<main>
  <div class="abs content-card"></div>
  <div class="abs hero" role="img" aria-label="Banner photo: laptop with a padlock in front of a glowing blue world map with network lines"></div>
  <p class="abs hero-caption">Duis aute irure dolor sitlum repehder invoptate velitese cillum dolore fugiat. Sunt in culpa deserunt.</p>

  <div class="abs section-band"></div>
  <h2 class="abs section-title" style="left:122px">About Us</h2>
  <h2 class="abs section-title" style="left:453px">Our Associates</h2>
  <h2 class="abs section-title" style="left:782px">Practice Areas</h2>

  <p class="abs about-text">Porta fusce varium natoque penatibus magnis. Montes nascetr mugiat suada odio. Porta fusce varium natoque penatibus magnis. Montes nascetr mugiat suada odio. Porta fusce varium natoque penatibus magnis. Montes nascetr mugiat suada odio. Porta fusce varium natoque penatibus magnis. Montes nascetr mugiat suada odio. varium natoque penatibus magnis. Montes nascetr mugiat suada odio.</p>

  <ul class="abs associates-list">
    <li>Kerode Miaersy Berose</li>
    <li>Naserta Fasderase</li>
    <li>Buvenas</li>
    <li>Miaersy Berose Kerta</li>
  </ul>

  <ul class="abs practice-list">
    <li>Cyber Security</li>
    <li>Data Protection</li>
    <li>Compliance services</li>
    <li>International Due Diligence Investigations</li>
    <li>Country and Travel Risk Assessments</li>
    <li>General Background Investigations</li>
    <li>Physical Security Services</li>
  </ul>

  <a class="abs read-more" href="#" style="left:125px">Read more <svg width="24" height="12" viewBox="0 0 24 12"><path d="M0 6 H20 M15 1 L21 6 L15 11" stroke="#5b9bd0" stroke-width="2.5" fill="none"/></svg></a>
  <a class="abs read-more" href="#" style="left:468px;top:810px">Read more <svg width="24" height="12" viewBox="0 0 24 12"><path d="M0 6 H20 M15 1 L21 6 L15 11" stroke="#5b9bd0" stroke-width="2.5" fill="none"/></svg></a>
  <a class="abs read-more" href="#" style="left:796px;top:810px">Read more <svg width="24" height="12" viewBox="0 0 24 12"><path d="M0 6 H20 M15 1 L21 6 L15 11" stroke="#5b9bd0" stroke-width="2.5" fill="none"/></svg></a>
</main>

<footer>
  <h2 class="abs footer-title" style="left:131px">Contact Us</h2>
  <address class="abs footer-address" style="font-style:normal">
    Falkirk and Associates, LLC<br>P.O. Box 41927<br>Gaithersburg, MD 20871<br>USA
  </address>
  <div class="abs footer-divider"></div>
  <dl class="abs contact-lines">
    <dt>Email:</dt><dd>gord@falkirkand associates.example</dd>
    <dt>Tel:</dt><dd>202-555-0147</dd>
  </dl>

  <h2 class="abs footer-title" style="left:889px">Follow Us</h2>
  <div class="abs social" style="top:917px"><span class="dot"></span>Friendbook</div>
  <div class="abs social" style="top:956px"><span class="dot"></span>Chirper</div>

  <p class="abs copyright">Copyright 2011 Falkirk &amp; Associate. LLC All rightts reserved</p>
</footer>

</body>
</html>
```